Bramble Hollow Networks - Electrical

We need flyers for electrical services.
Areas of work include new builds, office fitouts, switchboard upgrades, installation of ceiling fans, powerpoint and downlight upgrades, home theatre and AV systems, all exterior and emergency work. Free quotes
We would like to see designs with the colour Red with a young and modern design. Licence No: 63914K must be included and call Leopold on 0438917062.

Colors
ec1f27

```html
<!DOCTYPE html>
<html lang="en">
<head>
<meta charset="utf-8">
<title>Bramble Hollow Networks – Electrical Services Flyer</title>
<link href="https://fonts.googleapis.com/css2?family=Anton&family=Lato:wght@400;700&display=swap" rel="stylesheet">
<style>
  :root {
    --red: #ec1f27;
    --red-deep: #a8111a;
    --red-dark: #7d0b12;
    --navy: #1d2130;
    --ink: #1f1f24;
    --white: #ffffff;
    --paper: #e9e6e3;
    --photo-a: #c9ced6;
    --photo-b: #6f7a88;
  }
  * { margin: 0; padding: 0; box-sizing: border-box; }
  html, body { width: 1120px; height: 1200px; overflow: hidden; background: var(--paper); }
  .canvas { position: relative; width: 1120px; height: 1200px; }
  .flyer {
    position: absolute; left: 135px; top: 0;
    width: 850px; height: 1200px; background: var(--white); overflow: hidden;
    font-family: "Lato", sans-serif;
  }
  .flyer-shapes { position: absolute; inset: 0; }
  .headline {
    position: absolute; left: 48px; top: 66px;
    font-family: "Anton", sans-serif; font-size: 84px; line-height: 84px;
    letter-spacing: -0.5px; text-transform: uppercase;
  }
  .headline .line-one { display: block; color: var(--navy); }
  .headline .line-two { display: block; color: var(--red); margin-top: -4px; }
  .service-list {
    position: absolute; left: 48px; top: 330px; list-style: none;
    color: var(--white); font-weight: 700; font-size: 21px; line-height: 29px;
  }
  .service-list li::before { content: "\25CF"; font-size: 13px; margin-right: 7px; vertical-align: 3px; }
  .intro {
    position: absolute; left: 42px; top: 788px; width: 430px;
    color: var(--ink); font-size: 18px; line-height: 24.5px;
  }
  .divider { position: absolute; left: 40px; top: 968px; width: 455px; height: 3px; background: var(--red); }
  .licence {
    position: absolute; left: 40px; top: 988px; width: 440px;
    color: var(--ink); font-size: 20px; line-height: 26px;
  }
  .licence strong { font-weight: 700; }
  .contact-line {
    position: absolute; left: 44px; top: 1115px;
    color: var(--white); font-weight: 700; font-size: 21px;
  }
</style>
</head>
<body>
<div class="canvas">
  <div class="flyer">
    <svg class="flyer-shapes" viewBox="0 0 850 1200" width="850" height="1200">
      <defs>
        <linearGradient id="redBand" x1="0" y1="0" x2="1" y2="0">
          <stop offset="0" stop-color="var(--red-dark)"/>
          <stop offset="0.6" stop-color="var(--red-deep)"/>
          <stop offset="1" stop-color="var(--red)"/>
        </linearGradient>
        <linearGradient id="photoTone" x1="0" y1="0" x2="1" y2="1">
          <stop offset="0" stop-color="var(--photo-a)"/>
          <stop offset="1" stop-color="var(--photo-b)"/>
        </linearGradient>
      </defs>

      <rect class="service-band" x="0" y="285" width="850" height="345" fill="url(#redBand)"/>
      <polygon points="560,0 850,0 850,245" fill="var(--red)"/>
      <polygon points="700,0 850,0 850,150" fill="var(--red-deep)"/>
      <rect x="460" y="600" width="390" height="600" fill="var(--red)"/>
      <polygon points="850,260 850,700 640,480" fill="var(--red-deep)"/>
      <path d="M0,630 H470 L505,690 H0 Z" fill="var(--white)"/>
      <path d="M0,690 H505 L540,748 H0 Z" fill="var(--red-dark)"/>
      <path d="M0,748 H455 Q470,748 478,762 L575,930 V1075 H0 Z" fill="var(--white)"/>
      <polygon points="575,1030 850,1200 720,1200 575,1110" fill="var(--white)"/>
      <rect x="0" y="1075" width="850" height="125" fill="url(#redBand)"/>

      <g stroke="var(--white)" stroke-width="12" stroke-linejoin="round">
        <polygon points="590,10 796,252 577,494 356,252" fill="var(--white)"/>
        <polygon points="844,278 1040,474 838,670 648,474" fill="var(--white)"/>
        <polygon points="624,494 800,679 629,880 437,679" fill="var(--white)"/>
      </g>
      <g stroke-linejoin="round">
        <polygon role="img" aria-label="Photo: technician with clipboard inspecting switchgear cabinets" points="590,22 784,252 577,482 368,252" fill="url(#photoTone)" stroke="url(#photoTone)" stroke-width="10"/>
        <polygon role="img" aria-label="Photo: electrician working on a panel" points="844,290 1028,474 838,658 660,474" fill="url(#photoTone)" stroke="url(#photoTone)" stroke-width="10"/>
        <polygon role="img" aria-label="Photo: hands wiring terminal blocks" points="624,506 788,679 629,868 449,679" fill="url(#photoTone)" stroke="url(#photoTone)" stroke-width="10"/>
      </g>
      <circle cx="624" cy="1030" r="128" fill="var(--white)"/>
      <circle role="img" aria-label="Photo: electrician connecting switchboard wiring" cx="624" cy="1030" r="116" fill="url(#photoTone)"/>
    </svg>

    <h1 class="headline">
      <span class="line-one">Electrical</span>
      <span class="line-two">Services</span>
    </h1>

    <ul class="service-list">
      <li>New Builds</li>
      <li>Office Fitouts</li>
      <li>Switchboard Upgrades</li>
      <li>Installation of Ceiling Fans</li>
      <li>Powerpoint</li>
      <li>Downlight Upgrades</li>
      <li>Home Theatre</li>
      <li>AV Systems</li>
      <li>All Exterior and Emergency Work.</li>
    </ul>

    <p class="intro">Bramble Hollow Networks delivers safe, reliable electrical work for homes and businesses, from new builds and office fitouts to switchboard, powerpoint and downlight upgrades. We also install ceiling fans, home theatre and AV systems. Free quotes on every job.</p>

    <div class="divider"></div>

    <p class="licence"><strong>Licence No:</strong> 63914K<br>Call Leopold on 0438917062 for your free quote today.</p>

    <p class="contact-line">Ph: 0438917062 | W: bramblehollowelectrical.com</p>
  </div>
</div>
</body>
</html>
```